Wordpress Template for Food Retail Shop

We need a wordpress template that fits our new wp installation with about 6-7 sites. frontpage, news, team, products, contact. we provide food from local suppliers, * green * products. we provide a local bakery

```html
<!DOCTYPE html>
<html lang="en">
<head>
<meta charset="utf-8">
<title>Verdella – Local Bakery &amp; Green Food</title>
<link href="https://fonts.googleapis.com/css2?family=Catamaran:wght@500;600;700&family=Lato:wght@400;700&display=swap" rel="stylesheet">
<style>
:root{
  --green:#7dbb2f;
  --green-dark:#6aa322;
  --orange:#f6ab36;
  --ink:#2b2b2b;
  --text:#555;
  --muted:#777;
  --dark:#2a2a2a;
  --light:#f5f5f5;
  --white:#fff;
}
*{margin:0;padding:0;box-sizing:border-box}
html,body{width:1200px;height:3799px;overflow:hidden;background:var(--white)}
body{font-family:"Lato",sans-serif;color:var(--text);position:relative}
.abs{position:absolute}
h1,h2,h3,.brand{font-family:"Catamaran",sans-serif}
.ph{position:absolute;display:block}
.btn{position:absolute;display:flex;align-items:center;justify-content:center;border-radius:20px;color:#fff;font-size:14px;text-decoration:none}
.btn-green{background:var(--green)}
.btn-orange{background:var(--orange)}
.brand{display:flex;align-items:center;gap:10px;font-weight:700;color:var(--green);letter-spacing:.5px}
.brand .mark{border-radius:50%;background:var(--orange)}

/* header */
.site-header{position:absolute;left:0;top:0;width:1200px;height:116px;background:#fff}
.site-header .brand{position:absolute;left:80px;top:30px;font-size:46px;line-height:56px}
.site-header .mark{width:56px;height:56px}
.nav{position:absolute;top:50px;left:0;width:1200px;font-size:14px;color:#444}
.nav a{position:absolute;color:#444;text-decoration:none}
.nav a.active{color:var(--green)}
.nav a.active::after{content:"";position:absolute;left:0;right:0;top:26px;height:2px;background:var(--green)}

/* hero */
.hero{position:absolute;left:0;top:116px;width:1200px;height:640px;background:linear-gradient(100deg,#6b5a45 0%,#a88a63 30%,#5d4a36 60%,#3d3024 100%)}
.hero-text{position:absolute;left:644px;top:236px;color:#fff}
.hero-text .eyebrow{font-family:"Catamaran",sans-serif;font-weight:700;font-size:23px;line-height:26px}
.hero-text h1{font-size:44px;font-weight:700;line-height:50px;margin-top:2px}
.hero-text p{font-size:13px;line-height:16px;width:400px;margin-top:8px;margin-left:3px}
.hero .arrow{position:absolute;top:290px}
.dots{position:absolute;display:flex;gap:6px}
.dots i{width:8px;height:8px;border-radius:50%;background:#fff;opacity:.7}
.dots i.on{opacity:1}
.torn{position:absolute;left:0;width:1200px}

/* sections */
.section-title{position:absolute;left:0;width:1200px;text-align:center;font-size:38px;font-weight:600;color:var(--ink)}
.section-sub{position:absolute;left:0;width:1200px;text-align:center;font-size:13px;line-height:16px;color:#555}
.slider-arrows{position:absolute;display:flex;gap:12px}
.slider-arrows span{width:30px;height:30px;border:1px solid #999;border-radius:50%;display:flex;align-items:center;justify-content:center}

.about-title{position:absolute;left:635px;top:835px;font-size:32px;font-weight:600;color:var(--ink)}
.about-copy{position:absolute;left:635px;top:906px;width:490px;font-size:13px;line-height:16px;color:#444}
.about-copy p{margin-bottom:17px}

.product-name{position:absolute;width:324px;text-align:center;font-weight:700;font-size:15px;color:#333}

.testimonials{position:absolute;left:0;top:1842px;width:1200px;height:406px;background:var(--orange)}
.testimonials h2{position:absolute;left:0;width:1200px;top:54px;text-align:center;color:#fff;font-size:38px;font-weight:600}
.quote-name{position:absolute;left:528px;top:144px;color:#fff;font-family:"Catamaran",sans-serif;font-size:20px;font-weight:600}
.quote-role{position:absolute;left:526px;top:170px;color:#fff;font-family:"Catamaran",sans-serif;font-size:16px;font-weight:600}
.quote-text{position:absolute;left:533px;top:220px;width:515px;color:#fff;font-size:12px;line-height:15px}
.stars{position:absolute;left:532px;top:282px;display:flex;gap:5px}

.member-name{position:absolute;width:220px;text-align:center;font-family:"Catamaran",sans-serif;font-weight:600;font-size:17px;color:#333}
.member-role{position:absolute;width:220px;text-align:center;font-size:14px;color:#666}

.news-card{position:absolute;top:2865px;width:336px;height:375px;background:var(--light)}
.news-card .ph{left:10px;top:9px;width:316px;height:196px}
.news-date{position:absolute;left:20px;top:216px;color:var(--green);font-family:"Catamaran",sans-serif;font-size:17px;font-weight:600}
.news-title{position:absolute;left:20px;top:238px;color:#222;font-family:"Catamaran",sans-serif;font-size:18px;font-weight:600}
.news-text{position:absolute;left:20px;top:268px;width:290px;font-size:12.5px;line-height:15px;color:#555}
.news-more{position:absolute;left:20px;top:337px;font-size:13px;color:#555;display:flex;align-items:center;gap:6px}

.site-footer{position:absolute;left:0;top:3375px;width:1200px;height:343px;background:var(--dark);color:#fff}
.site-footer .brand{position:absolute;left:80px;top:80px;font-size:50px;line-height:60px}
.site-footer .mark{width:58px;height:58px}
.footer-about{position:absolute;left:80px;top:158px;width:240px;font-size:14px;line-height:17px}
.footer-more{position:absolute;left:78px;top:239px;font-size:15px}
.footer-head{position:absolute;top:76px;font-size:16px;font-weight:700}
.footer-head::after{content:"";position:absolute;left:0;top:31px;width:100%;height:2px;background:#fff}
.footer-links{position:absolute;left:405px;top:135px;list-style:none;font-size:13px}
.footer-links li{height:24px}
.footer-links li::before{content:"›";margin-right:9px}
.contact-row{position:absolute;left:569px;font-size:14px}
.contact-row b{font-weight:400;display:inline-block;width:77px}
.gallery .ph{width:87px;height:61px}
.copyright{position:absolute;left:80px;top:3746px;font-size:13px;color:#444}
.social{position:absolute;top:3738px;width:32px;height:32px;border-radius:50%}
</style>
</head>
<body>

<header class="site-header">
  <div class="brand"><span class="mark"></span>Verdella</div>
  <nav class="nav">
    <a class="active" style="left:625px">Home</a>
    <a style="left:700px">About us</a>
    <a style="left:792px">Products</a>
    <a style="left:883px">News</a>
    <a style="left:955px">Team</a>
    <a style="left:1024px">Contact</a>
    <svg class="abs" style="left:1106px;top:2px" width="16" height="16" viewBox="0 0 16 16"><circle cx="6.5" cy="6.5" r="5" fill="none" stroke="#333" stroke-width="1.6"/><line x1="10.5" y1="10.5" x2="15" y2="15" stroke="#333" stroke-width="1.6"/></svg>
  </nav>
</header>

<section class="hero">
  <span class="ph" role="img" aria-label="Smiling baker holding a tray of sandwiches in a bakery" style="left:0;top:0;width:1200px;height:640px;background:linear-gradient(90deg,rgba(0,0,0,0) 40%,rgba(0,0,0,.25) 100%)"></span>
  <svg class="arrow" style="left:28px" width="14" height="24" viewBox="0 0 14 24"><polyline points="12,2 2,12 12,22" fill="none" stroke="#fff" stroke-width="2"/></svg>
  <svg class="arrow" style="left:1148px" width="14" height="24" viewBox="0 0 14 24"><polyline points="2,2 12,12 2,22" fill="none" stroke="#fff" stroke-width="2"/></svg>
  <div class="hero-text">
    <div class="eyebrow">We Create</div>
    <h1>Delicious Memories</h1>
    <p>Lorem Ipsum is simply dummy text of the printing typesetting industry's standard dummy text ever since the 1500s,</p>
  </div>
  <a class="btn btn-orange" style="left:646px;top:363px;width:174px;height:37px">Read More</a>
  <div class="dots" style="left:573px;top:564px"><i class="on"></i><i></i><i></i><i></i></div>
</section>
<svg class="torn" style="top:720px" height="40" viewBox="0 0 1200 40" preserveAspectRatio="none"><path d="M0 20 L30 14 L55 24 L80 12 L110 22 L140 15 L170 25 L200 13 L230 21 L260 16 L290 26 L320 12 L350 22 L380 17 L410 24 L440 13 L470 21 L500 15 L530 25 L560 14 L590 22 L620 16 L650 24 L680 12 L710 21 L740 17 L770 25 L800 14 L830 22 L860 16 L890 24 L920 13 L950 22 L980 15 L1010 25 L1040 14 L1070 22 L1100 17 L1130 24 L1160 13 L1200 20 L1200 40 L0 40Z" fill="#fff"/></svg>

<!-- About -->
<section class="about">
  <span class="ph" role="img" aria-label="Pizza and burgers on a wooden table" style="left:80px;top:828px;width:281px;height:204px;background:linear-gradient(135deg,#c98a4a,#8a4a22 60%,#d8b07a)"></span>
  <span class="ph" role="img" aria-label="Crepes dusted with sugar and a cup of cream" style="left:380px;top:904px;width:193px;height:249px;background:linear-gradient(160deg,#7a4b22,#d79a4d 55%,#b5722f)"></span>
  <span class="ph" role="img" aria-label="Wrap filled with vegetables on a board" style="left:212px;top:1051px;width:149px;height:152px;background:linear-gradient(180deg,#2a2522,#9c6b3f 70%,#5a3a22)"></span>
  <h2 class="about-title">About us</h2>
  <div class="about-copy">
    <p>Lorem Ipsum is simply dummy text of the printing and typesetting industry. Lorem Ipsum has been the industry's standard dummy text ever since the 1500s,</p>
    <p>when an unknown printer took a galley of type and scrambled it to make a type specimen book. It has survived not only five centuries, but also the leap into electronic typesetting, remaining essentially unchanged.</p>
    <p>It was popularised in the 1960s with the release of Letraset sheets containing Lorem Ipsum passages, a</p>
  </div>
  <a class="btn btn-green" style="left:636px;top:1095px;width:174px;height:40px">Read More</a>
</section>

<!-- Products -->
<section class="products">
  <h2 class="section-title" style="top:1272px">Our Products</h2>
  <p class="section-sub" style="top:1324px">Lorem Ipsum is simply dummy text of the printing and<br>typesetting industry</p>
  <div class="slider-arrows" style="left:1047px;top:1319px">
    <span><svg width="8" height="12" viewBox="0 0 8 12"><polyline points="6,1 1,6 6,11" fill="none" stroke="#777" stroke-width="1.3"/></svg></span>
    <span><svg width="8" height="12" viewBox="0 0 8 12"><polyline points="2,1 7,6 2,11" fill="none" stroke="#777" stroke-width="1.3"/></svg></span>
  </div>
  <span class="ph" role="img" aria-label="Tongs lifting pastries from a tray" style="left:80px;top:1381px;width:324px;height:301px;background:linear-gradient(150deg,#e9d2a8,#b87a36 50%,#e6c995)"></span>
  <span class="ph" role="img" aria-label="Baker holding a stand of croissants" style="left:438px;top:1381px;width:324px;height:301px;background:linear-gradient(150deg,#f2f2f2,#c48540 55%,#9aa6b4)"></span>
  <span class="ph" role="img" aria-label="Sandwich with lettuce, tomato and onion" style="left:796px;top:1381px;width:323px;height:301px;background:linear-gradient(150deg,#f1ebd8,#d4a462 45%,#6a9a3a 65%,#b8a79a)"></span>
  <div class="product-name" style="left:66px;top:1694px">Products Name</div>
  <div class="product-name" style="left:442px;top:1694px">Products Name</div>
  <div class="product-name" style="left:800px;top:1694px">Products Name</div>
  <a class="btn btn-green" style="left:516px;top:1739px;width:174px;height:39px">View More</a>
</section>

<!-- Testimonials -->
<svg class="torn" style="top:1826px" height="18" viewBox="0 0 1200 18" preserveAspectRatio="none"><path d="M0 18 L0 10 L40 14 L70 6 L100 12 L140 5 L180 13 L220 7 L260 12 L300 4 L340 11 L380 6 L420 13 L460 5 L500 12 L540 7 L580 13 L620 4 L660 11 L700 6 L740 12 L780 5 L820 13 L860 7 L900 12 L940 4 L980 11 L1020 6 L1060 13 L1100 5 L1140 12 L1200 8 L1200 18Z" fill="#f6ab36"/></svg>
<section class="testimonials">
  <h2>Testimonials</h2>
  <svg class="abs" style="left:282px;top:140px" width="40" height="90" viewBox="0 0 40 90"><circle cx="20" cy="6" r="4" fill="#fff"/><circle cx="12" cy="27" r="6" fill="#fff"/><circle cx="16" cy="55" r="12" fill="#fff"/></svg>
  <span class="ph" role="img" aria-label="Portrait of a smiling customer" style="left:302px;top:123px;width:186px;height:186px;border-radius:50%;border:4px solid #fff;background:radial-gradient(circle at 50% 40%,#f3f3f3,#c9b5a4 70%,#8b6b55)"></span>
  <div class="quote-name">Marla Quint</div>
  <div class="quote-role">Creative Director</div>
  <svg class="abs" style="left:520px;top:204px" width="16" height="12" viewBox="0 0 16 12"><text x="0" y="14" fill="#fff" font-size="22" font-family="Georgia,serif">“</text></svg>
  <p class="quote-text">Lorem Ipsum&nbsp; simply dummy text the printing and ypesetting industry&nbsp; simply dummy Ipsum is simply dummy text of the printing.Lorem Ipsum&nbsp; simply dummy text a printing simply dummy Ipsum is simply dummy text of the in the industries printing.</p>
  <svg class="abs" style="left:984px;top:260px" width="16" height="14" viewBox="0 0 16 14"><text x="0" y="22" fill="#fff" font-size="22" font-family="Georgia,serif">”</text></svg>
  <div class="stars">
    <svg width="86" height="16" viewBox="0 0 86 16"><g fill="#fff"><path id="st" d="M8 0l2.4 5 5.4.6-4 3.7 1.1 5.4L8 12l-4.9 2.7 1.1-5.4-4-3.7 5.4-.6z"/><use href="#st" x="17.5"/><use href="#st" x="35"/><use href="#st" x="52.5"/><use href="#st" x="70"/></g></svg>
  </div>
  <div class="dots" style="left:582px;top:354px"><i style="background:var(--green);opacity:1"></i><i></i><i></i></div>
</section>
<svg class="torn" style="top:2246px" height="18" viewBox="0 0 1200 18" preserveAspectRatio="none"><path d="M0 0 L1200 0 L1200 8 L1160 13 L1120 5 L1080 12 L1040 6 L1000 14 L960 7 L920 12 L880 4 L840 11 L800 6 L760 13 L720 5 L680 12 L640 7 L600 14 L560 4 L520 11 L480 6 L440 12 L400 5 L360 13 L320 7 L280 12 L240 4 L200 11 L160 6 L120 13 L80 5 L40 12 L0 8Z" fill="#f6ab36"/></svg>

<!-- Team -->
<section class="team">
  <h2 class="section-title" style="top:2314px">Our Team</h2>
  <p class="section-sub" style="top:2370px">Lorem Ipsum is simply dummy text of the printing and<br>typesetting industry</p>
  <div class="slider-arrows" style="left:1047px;top:2352px">
    <span><svg width="8" height="12" viewBox="0 0 8 12"><polyline points="6,1 1,6 6,11" fill="none" stroke="#777" stroke-width="1.3"/></svg></span>
    <span><svg width="8" height="12" viewBox="0 0 8 12"><polyline points="2,1 7,6 2,11" fill="none" stroke="#777" stroke-width="1.3"/></svg></span>
  </div>
  <span class="ph" role="img" aria-label="Chef in white uniform with arms crossed" style="left:115px;top:2432px;width:170px;height:265px;background:linear-gradient(180deg,#fff 0%,#eceff2 40%,#d7dde3 100%)"></span>
  <span class="ph" role="img" aria-label="Chef in white uniform with arms crossed" style="left:381px;top:2432px;width:170px;height:265px;background:linear-gradient(180deg,#fff 0%,#eceff2 40%,#d7dde3 100%)"></span>
  <span class="ph" role="img" aria-label="Chef holding a wooden spoon" style="left:650px;top:2432px;width:170px;height:265px;background:linear-gradient(180deg,#fff 0%,#eceff2 40%,#d7dde3 100%)"></span>
  <span class="ph" role="img" aria-label="Chef in white uniform with arms crossed" style="left:922px;top:2432px;width:170px;height:265px;background:linear-gradient(180deg,#fff 0%,#eceff2 40%,#d7dde3 100%)"></span>
  <div class="member-name" style="left:87px;top:2710px">Oriana Pell</div>
  <div class="member-role" style="left:91px;top:2734px">Owner</div>
  <div class="member-name" style="left:353px;top:2710px">Delia Hawthorn</div>
  <div class="member-role" style="left:353px;top:2734px">Project Manager</div>
  <div class="member-name" style="left:626px;top:2710px">Corinne</div>
  <div class="member-role" style="left:626px;top:2734px">Manager</div>
  <div class="member-name" style="left:893px;top:2710px">Tobin Garrow</div>
  <div class="member-role" style="left:897px;top:2734px">Manager</div>
</section>

<!-- News -->
<section class="news">
  <h2 class="section-title" style="top:2806px">Latest News</h2>
  <article class="news-card" style="left:71px">
    <span class="ph" role="img" aria-label="Grilled sandwich on a wooden board" style="background:linear-gradient(180deg,#1e1c1b,#b5642a 50%,#5a3a20)"></span>
    <div class="news-date">Oct 22, 2019</div>
    <h3 class="news-title">BEST FLAVORS</h3>
    <p class="news-text">Lorem Ipsum is simply dummy text of the print and typesetting industry. Lorem Ipsum has been in the industry's.</p>
    <div class="news-more">Read More.. <svg width="14" height="14" viewBox="0 0 14 14"><circle cx="7" cy="7" r="6" fill="none" stroke="#555"/><polyline points="6,4 9,7 6,10" fill="none" stroke="#555"/></svg></div>
  </article>
  <article class="news-card" style="left:432px">
    <span class="ph" role="img" aria-label="Seeded pastries on a dark surface" style="background:linear-gradient(180deg,#2a2a2a,#a47a48 50%,#3a3228)"></span>
    <div class="news-date">Oct 22, 2019</div>
    <h3 class="news-title">BEST FLAVORS</h3>
    <p class="news-text">Lorem Ipsum is simply dummy text of the print and typesetting industry. Lorem Ipsum has been in the industry's.</p>
    <div class="news-more">Read More.. <svg width="14" height="14" viewBox="0 0 14 14"><circle cx="7" cy="7" r="6" fill="none" stroke="#555"/><polyline points="6,4 9,7 6,10" fill="none" stroke="#555"/></svg></div>
  </article>
  <article class="news-card" style="left:792px">
    <span class="ph" role="img" aria-label="Croissants on a linen cloth" style="background:linear-gradient(180deg,#3c4148,#cf8b3e 50%,#4a4d52)"></span>
    <div class="news-date">Oct 22, 2019</div>
    <h3 class="news-title">BEST FLAVORS</h3>
    <p class="news-text">Lorem Ipsum is simply dummy text of the print and typesetting industry. Lorem Ipsum has been in the industry's.</p>
    <div class="news-more">Read More.. <svg width="14" height="14" viewBox="0 0 14 14"><circle cx="7" cy="7" r="6" fill="none" stroke="#555"/><polyline points="6,4 9,7 6,10" fill="none" stroke="#555"/></svg></div>
  </article>
  <a class="btn btn-green" style="left:516px;top:3266px;width:174px;height:39px">View More</a>
</section>

<!-- Footer -->
<svg class="torn" style="top:3358px" height="18" viewBox="0 0 1200 18" preserveAspectRatio="none"><path d="M0 18 L0 10 L30 13 L60 6 L90 12 L130 5 L170 13 L210 7 L250 12 L290 4 L330 11 L370 6 L410 13 L450 5 L490 12 L530 7 L570 13 L610 4 L650 11 L690 6 L730 12 L770 5 L810 13 L850 7 L890 12 L930 4 L970 11 L1010 6 L1050 13 L1090 5 L1130 12 L1170 7 L1200 10 L1200 18Z" fill="#2a2a2a"/></svg>
<footer class="site-footer">
  <div class="brand"><span class="mark"></span>Verdella</div>
  <p class="footer-about">Lorem Ipsum is simply dummy in text of the printing and typesetting in the industry Lorem Ipsum</p>
  <div class="footer-more">Read More..<svg width="11" height="11" viewBox="0 0 14 14" style="margin-left:2px"><circle cx="7" cy="7" r="6" fill="none" stroke="#fff"/><polyline points="6,4 9,7 6,10" fill="none" stroke="#fff"/></svg></div>

  <div class="footer-head" style="left:405px">Quick Link</div>
  <ul class="footer-links">
    <li>Home</li><li>About us</li><li>Products</li><li>News</li><li>Team</li><li>Contact</li>
  </ul>

  <div class="footer-head" style="left:569px">Contact us</div>
  <div class="contact-row" style="top:137px"><b>Address :</b>48 Millbrook Lane,</div>
  <div class="contact-row" style="top:166px"><b></b>Fernvale, Westshire</div>
  <div class="contact-row" style="top:194px"><b></b>Zipcode</div>
  <div class="contact-row" style="top:224px"><b>Phone&nbsp;&nbsp;&nbsp;:</b>+00 555 0142</div>
  <div class="contact-row" style="top:252px"><b>E-mail&nbsp;&nbsp;&nbsp;:</b>hello@verdella.example</div>

  <div class="footer-head" style="left:846px">Gallery</div>
  <div class="gallery">
    <span class="ph" role="img" aria-label="Bread rolls" style="left:845px;top:135px;background:linear-gradient(135deg,#d89a54,#8a5322)"></span>
    <span class="ph" role="img" aria-label="Sliced cake" style="left:939px;top:135px;background:linear-gradient(135deg,#b06a3a,#e6c7a0)"></span>
    <span class="ph" role="img" aria-label="Spiral pastries" style="left:1033px;top:135px;background:linear-gradient(135deg,#4a6a3a,#d2a062)"></span>
    <span class="ph" role="img" aria-label="Baked pie" style="left:845px;top:204px;background:linear-gradient(135deg,#e0b060,#9b6a2a)"></span>
    <span class="ph" role="img" aria-label="Cheese tart" style="left:939px;top:204px;background:linear-gradient(135deg,#f0d27a,#b8862e)"></span>
    <span class="ph" role="img" aria-label="Pastry slices" style="left:1033px;top:204px;background:linear-gradient(135deg,#e8c48a,#c47a3a)"></span>
  </div>
</footer>

<div class="copyright">Copyright © Verdella 2019. All Right Reserved.</div>
<span class="social" aria-label="Social link" style="left:970px;background:var(--green)"></span>
<span class="social" aria-label="Social link" style="left:1008px;background:var(--orange)"></span>
<span class="social" aria-label="Social link" style="left:1047px;background:var(--orange)"></span>
<span class="social" aria-label="Social link" style="left:1085px;background:var(--orange)"></span>

</body>
</html>
```